Website for Apartment Rental in Prague

I would like to create designs of my website focused on luxury apartment rentals in Prague, Czech Republic. I created initial mock-ups, They are all attached. I need to design homepage and subpage. The mock-ups were created by combining elements from different websites that I liked but I need you to create a design that is unique and original. The attached files a only a guidance for the structure of the website but not for the design. Try to be creative.

Industry/Entity Type

Apartment

```html
<!DOCTYPE html>
<html lang="en">
<head>
<meta charset="utf-8">
<title>Apartments Lumen – Luxury Apartment Rentals</title>
<link href="https://fonts.googleapis.com/css2?family=Raleway:wght@300;400;500;600;700&family=Open+Sans:wght@400;600&display=swap" rel="stylesheet">
<style>
:root{
  --ink:#1d1d1d;
  --text:#555;
  --muted:#8a8a8a;
  --line:#d9d9d9;
  --accent:#d9952f;
  --accent-soft:#f6c58a;
  --accent-pale:#fde3c4;
  --cream:#fdf6ee;
  --paper:#ffffff;
  --footer:#eeeeee;
}
*{box-sizing:border-box;margin:0;padding:0}
html,body{width:1200px;height:2799px;overflow:hidden;background:var(--paper)}
body{position:relative;font-family:"Open Sans",Arial,sans-serif;color:var(--ink)}
.abs{position:absolute}

/* wordmark: one colour, one weight, one plain square */
.wordmark{display:flex;align-items:center;gap:10px;font-family:"Raleway",sans-serif;font-weight:600;font-size:21px;color:var(--ink);white-space:nowrap}
.wordmark .mark{width:12px;height:12px;background:var(--ink)}

/* header */
.site-header{left:0;top:0;width:1200px;height:135px;background:var(--paper)}
.site-header .wordmark{left:80px;top:34px}
.top-links{right:76px;top:32px;font-size:13px;color:#333;display:flex;gap:15px}
.top-links span.sep{color:#999}
.main-nav{left:93px;top:95px;display:flex;font-size:15px;font-family:"Raleway",sans-serif;font-weight:600}
.main-nav a{color:var(--ink);text-decoration:none;margin-right:52px}

/* hero */
.hero{left:0;top:135px;width:1200px;height:798px;background:linear-gradient(180deg,#e9e9e7 0%,#dcdbd8 45%,#cfcdc9 100%)}
.hero-title{left:0;top:92px;width:1200px;text-align:center;font-family:"Raleway",sans-serif;font-weight:500;color:var(--ink)}
.hero-title .line1{font-size:52px;letter-spacing:10px;line-height:1}
.hero-title .line2{font-size:74px;letter-spacing:10px;line-height:1.15}
.hero-title .tag{font-size:38px;margin-top:6px;letter-spacing:0}
.hero-btns{left:0;top:312px;width:1200px;display:flex;justify-content:center;gap:14px}
.pill{background:var(--paper);border-radius:30px;padding:0 28px;height:50px;line-height:50px;font-size:16px;font-family:"Raleway",sans-serif;font-weight:600}
.booking{left:78px;top:428px;width:1042px;height:370px;background:rgba(255,255,255,.45);border:1px solid rgba(255,255,255,.8)}
.booking h2{position:absolute;left:0;top:66px;width:100%;text-align:center;font-family:"Raleway",sans-serif;font-weight:500;font-size:37px}
.field-label{font-size:13px;color:#444}
.field{background:var(--paper);border:1px solid var(--line);height:42px;font-size:13px;color:#aaa;padding:12px 10px}
.btn-orange{background:var(--accent-soft);border:2px solid #e9a75a;font-size:14px;height:42px;line-height:38px;text-align:center}

/* vision */
.section-title{left:0;width:1200px;text-align:center;font-family:"Raleway",sans-serif;font-weight:500;font-size:37px}
.lead{left:0;width:1200px;text-align:center;font-size:13.5px;line-height:23px;color:var(--text)}
.feature{width:312px;height:118px;border:2px solid #e3e3e3;background:var(--paper)}
.feature svg{position:absolute;left:30px;top:32px}
.feature h3{position:absolute;left:105px;top:12px;font-family:"Raleway",sans-serif;font-weight:500;font-size:23px}
.feature p{position:absolute;left:105px;top:46px;font-size:12.5px;line-height:20px;color:var(--muted);width:190px}

/* offers */
.offers{left:78px;top:1362px;width:1042px;height:527px;background:var(--cream)}
.offers-frame{left:12px;top:12px;width:1018px;height:503px;border:1px solid #f0d8b8}
.offer{top:118px;width:233px;height:332px;background:var(--paper);box-shadow:0 2px 6px rgba(0,0,0,.15)}
.offer .photo{position:absolute;left:4px;top:4px;width:225px;height:177px}
.offer h4{position:absolute;left:10px;top:192px;font-family:"Raleway",sans-serif;font-weight:700;font-size:18px;line-height:24px}
.offer .meta{position:absolute;left:10px;top:254px;font-size:10px;color:var(--muted);letter-spacing:1px}
.offer .details{position:absolute;left:10px;top:278px;width:213px;height:40px;border-radius:20px;background:linear-gradient(#f4f4f4,#dcdcdc);text-align:center;line-height:40px;font-family:"Raleway",sans-serif;font-weight:500;font-size:16px;letter-spacing:1px}
.arrow{top:1621px;width:50px;height:50px;border-radius:25px;background:#f5f5f5}

/* contact */
.contact-band{left:0;top:2157px;width:1200px;height:269px;background:linear-gradient(180deg,#d6d6d6,#ececec)}
.contact-band .input{position:absolute;top:155px;width:248px;height:50px;border-radius:25px;background:var(--paper);border:1px solid #ddd;padding:0 25px;line-height:50px;font-size:15px;color:#444}
.submit{position:absolute;left:896px;top:155px;width:196px;height:50px;border-radius:25px;background:var(--accent);color:#fff;text-align:center;line-height:50px;font-size:16px;font-family:"Raleway",sans-serif;font-weight:600}

/* footer */
.site-footer{left:0;top:2426px;width:1200px;height:310px;background:var(--footer)}
.site-footer .wordmark{left:80px;top:84px;font-size:19px}
.footer-col h5{font-family:"Raleway",sans-serif;font-weight:700;font-size:17px;color:#555;margin-bottom:14px}
.footer-col li{list-style:none;font-size:13px;color:#666;line-height:30px}
.footer-col li::before{content:"»";margin-right:10px;color:#888}
.contact-row{display:flex;align-items:center;gap:10px;font-size:13px;color:#666;margin-bottom:14px}
.copyright{left:0;top:2736px;width:1200px;height:63px;background:var(--accent);color:#fff;text-align:center;line-height:63px;font-size:14px}
</style>
</head>
<body>

<header class="site-header abs">
  <div class="wordmark abs"><span class="mark"></span>Apartments Lumen</div>
  <nav class="top-links abs"><span>Discover Prague</span><span class="sep">/</span><span>Our Hospitality</span><span class="sep">/</span><span>Chat Us</span><span class="sep">/</span><span>Call Us Now</span><span class="sep">/</span><span>EN</span></nav>
  <nav class="main-nav abs"><a>.Home</a><a>.Apartments</a><a>.Services</a><a>.Gallery</a><a>.News</a><a>.Exclusive Offers &amp; Tours</a><a>.For Families</a><a>.Contact</a></nav>
</header>

<section class="hero abs" role="img" aria-label="Bright white living room with large windows, sofa and bookshelf">
  <h1 class="hero-title abs">
    <div class="line1">APARTMENT</div>
    <div class="line2">LUMEN</div>
    <div class="tag">WE'LL HELP YOU FIND YOUR NEW HOME</div>
  </h1>
  <div class="hero-btns abs"><span class="pill">FIND OUT MORE</span><span class="pill">BOOK AN APPOINTMENT</span></div>
  <form class="booking abs">
    <h2>OFFICIAL SITE - BEST PRICE GUARANTEED</h2>
    <span class="field-label abs" style="left:60px;top:122px">Check in date</span>
    <div class="field abs" style="left:58px;top:146px;width:356px">11/17/2017</div>
    <span class="field-label abs" style="left:424px;top:122px">Check out date</span>
    <div class="field abs" style="left:422px;top:146px;width:356px">11/18/2017</div>
    <span class="field-label abs" style="left:790px;top:122px">Adults</span>
    <div class="field abs" style="left:788px;top:146px;width:60px">2</div>
    <span class="field-label abs" style="left:858px;top:122px">Children</span>
    <div class="field abs" style="left:856px;top:146px;width:60px">0</div>
    <span class="field-label abs" style="left:926px;top:122px">Infants</span>
    <div class="field abs" style="left:924px;top:146px;width:62px">0</div>
    <span class="field-label abs" style="left:60px;top:205px">Promotional code</span>
    <div class="field abs" style="left:58px;top:227px;width:416px"></div>
    <div class="btn-orange abs" style="left:480px;top:227px;width:156px">Check availability</div>
    <div class="btn-orange abs" style="left:641px;top:227px;width:342px;background:var(--accent-pale);text-align:left;padding-left:58px">Select Rental Unit</div>
    <div class="abs" style="left:643px;top:229px;width:42px;height:38px;background:var(--accent-soft);font-size:14px;line-height:38px;text-align:center">Or</div>
  </form>
</section>

<h2 class="section-title abs" style="top:994px">A DIFFERENT VISION OF TRAVELLING</h2>
<p class="lead abs" style="top:1056px">Something spectacular has arrived in the heart of Europe.<br>Steps from Old Town, this rental experience is curated with world-class amenities, exemplary style and a level of convenience you have to exprience to belive.<br>Experience the different visiov of luxury in center of Prague.</p>

<div class="feature abs" style="left:124px;top:1175px">
  <svg width="40" height="50" viewBox="0 0 40 50" fill="none" stroke="#888" stroke-width="2"><path d="M5 48V12l15-8 15 8v36"/><path d="M12 18h4M24 18h4M12 26h4M24 26h4M12 34h4M24 34h4M17 48v-7h6v7"/></svg>
  <h3>APARTMENTS</h3><p>also available to rent all the apartment together for companie or larger groups.</p>
</div>
<div class="feature abs" style="left:447px;top:1175px">
  <svg width="46" height="46" viewBox="0 0 46 46" fill="none" stroke="#888" stroke-width="2"><circle cx="23" cy="23" r="19"/><path d="M23 11v12l8 6"/></svg>
  <h3>CHECK-OUT</h3><p>12 noon; earliest check-in, 3pm- both are flexible, by arrangement.</p>
</div>
<div class="feature abs" style="left:770px;top:1175px">
  <svg width="46" height="46" viewBox="0 0 46 46" fill="none" stroke="#888" stroke-width="2"><path d="M4 24L24 4h16v16L20 40z"/><circle cx="32" cy="12" r="3"/></svg>
  <h3>RATES</h3><p>price from 150 USD per night, including tax.</p>
</div>

<section class="offers abs">
  <div class="offers-frame abs"></div>
  <h2 class="section-title abs" style="left:0;width:1042px;top:46px">EXCLUSIVE OFFERS</h2>
  <article class="offer abs" style="left:33px"><div class="photo" role="img" aria-label="Loft living room with arched windows" style="background:linear-gradient(135deg,#5a5048,#b9a896)"></div><h4>Brand New Modern<br>Apartment Location</h4><span class="meta">3 BEDS &nbsp;/&nbsp; 2 BATHS</span><span class="details">VIEW DETAILS</span></article>
  <article class="offer abs" style="left:286px"><div class="photo" role="img" aria-label="Bedroom with vaulted ceiling and warm lighting" style="background:linear-gradient(135deg,#7a4a2c,#d98a4a)"></div><h4>Brand New Modern<br>Apartment Location</h4><span class="meta">3 BEDS &nbsp;/&nbsp; 2 BATHS</span><span class="details">VIEW DETAILS</span></article>
  <article class="offer abs" style="left:539px"><div class="photo" role="img" aria-label="Minimal lounge with white sofas" style="background:linear-gradient(135deg,#8b8470,#d8d2bf)"></div><h4>Brand New Modern<br>Apartment Location</h4><span class="meta">3 BEDS &nbsp;/&nbsp; 2 BATHS</span><span class="details">VIEW DETAILS</span></article>
  <article class="offer abs" style="left:792px"><div class="photo" role="img" aria-label="Terrace lounge overlooking the city at sunset" style="background:linear-gradient(180deg,#e8a05a,#8a6a4a)"></div><h4>Brand New Modern<br>Apartment Location</h4><span class="meta">3 BEDS &nbsp;/&nbsp; 2 BATHS</span><span class="details">VIEW DETAILS</span></article>
</section>
<div class="arrow abs" style="left:-10px"><svg width="50" height="50"><path d="M28 19l-6 6 6 6" stroke="#333" stroke-width="2" fill="none"/></svg></div>
<div class="arrow abs" style="left:1160px"><svg width="50" height="50"><path d="M22 19l6 6-6 6" stroke="#e0a060" stroke-width="2" fill="none"/></svg></div>

<h2 class="section-title abs" style="top:1946px">INTERIORS DESIGNED BY MAISON CLAIR</h2>
<p class="lead abs" style="top:2006px;left:100px;width:1000px">Maison Clair apartments offers short term and as well &nbsp;as long term options in our studio apartments and our one bedroom apartment homes. Our luxurious apartments and high quality customer services have allowed us to domainate tha prague apartment market with a proven track record. Our years of experience and knowledge have made us a premier apartment rental company as we continue to stress the importance of servicimg individuals and corporations who are seeking the finestaccommodations.</p>

<section class="contact-band abs" role="img" aria-label="Faded city skyline">
  <h2 class="section-title abs" style="top:46px">CONTACT US NOW</h2>
  <p class="lead abs" style="top:110px">Maison Clair apartments offers short term and as well &nbsp;as long term options in our studio apartments and our one bedroom</p>
  <div class="input" style="left:116px">Name</div>
  <div class="input" style="left:376px">Email</div>
  <div class="input" style="left:636px">Other Detail</div>
  <div class="submit">SUBMIT</div>
</section>

<footer class="site-footer abs">
  <div class="wordmark abs"><span class="mark"></span>Apartments Lumen</div>
  <p class="abs" style="left:80px;top:144px;width:215px;font-size:13px;line-height:24px;color:#555">Maison Clair apartments offers short term and as well &nbsp;as long term options in our studio apartment.</p>
  <div class="footer-col abs" style="left:345px;top:64px"><h5>Quick Links</h5><ul><li>Home</li><li>About Us</li><li>Services</li><li>Gallery</li><li>News</li><li>Contact Us</li></ul></div>
  <div class="footer-col abs" style="left:623px;top:64px;width:240px"><h5>Get In Touch</h5>
    <div class="contact-row" style="align-items:flex-start"><svg width="20" height="20" viewBox="0 0 20 20" fill="none" stroke="#777" stroke-width="2"><path d="M10 1v18M3 5h14M3 10h14"/></svg><span><b style="font-family:Raleway,sans-serif;color:#666">APARTMENT LUMEN</b><br>123,Lorem ipsum dummy text,<br>Country-123456.</span></div>
    <div class="contact-row"><svg width="20" height="20" viewBox="0 0 20 20" fill="#777"><path d="M4 2l4 1 1 4-2 2a11 11 0 0 0 4 4l2-2 4 1 1 4-3 2C8 17 3 12 2 5z"/></svg>+420 600 123 456</div>
    <div class="contact-row"><svg width="20" height="16" viewBox="0 0 20 16" fill="none" stroke="#777" stroke-width="2"><rect x="1" y="1" width="18" height="14"/><path d="M1 1l9 8 9-8"/></svg>reservation@lumenstay.example</div>
  </div>
  <div class="footer-col abs" style="left:876px;top:64px"><h5>Map</h5>
    <div role="img" aria-label="Street map showing the apartment location" style="width:247px;height:178px;background:linear-gradient(135deg,#e6e2d8 0%,#e6e2d8 45%,#9fc3e6 55%,#9fc3e6 100%);border:1px solid #ccc"></div>
  </div>
</footer>

<div class="copyright abs">© <b>APARTMENT LUMEN</b> - 2017. All Rights Reserved</div>

</body>
</html>
```